Business Card Design for Occupational Medicine Start Up Company

We need to design a professional business card. We are a healthcare company providing occupational medicine services to blue collar industries. We are professional, efficient and high quality service providers.

Target Market(s)

Blue Collar Industry: Shipbuilding, Ports, Trucking Companies; The Executives and Safety Officers for these companies

Industry/Entity Type

Healthcare

Contact Information for Business Card

Logo, Name, Title, Email, Phone

Other font styles liked:
• Please match our Brand Guide

Requirements
Must have
• Our Company Colors and Logo

```html
<!DOCTYPE html>
<html lang="en">
<head>
<meta charset="UTF-8">
<title>Harborline Care — Business Card</title>
<link rel="stylesheet" href="https://fonts.googleapis.com/css2?family=Montserrat:wght@400;600;700&family=Arimo:wght@400;700&display=swap">
<style>
  :root {
    --bg: #ececea;
    --card-navy: #2d3480;
    --accent-blue: #36a4e0;
    --text-white: #ffffff;
    --rule: rgba(255,255,255,0.55);
    --brand-font: "Montserrat", sans-serif;
    --body-font: "Arimo", sans-serif;
  }
  * { box-sizing: border-box; margin: 0; padding: 0; }
  html, body { width: 1200px; height: 802px; overflow: hidden; }
  body {
    background: var(--bg);
    display: flex;
    align-items: center;
    justify-content: center;
    gap: 40px;
    font-family: var(--body-font);
    color: var(--text-white);
  }
  .card {
    width: 540px;
    height: 309px;
    background: var(--card-navy);
    position: relative;
    box-shadow: 0 6px 18px rgba(0,0,0,0.18);
    flex: none;
  }

  /* Front */
  .card-front { display: flex; align-items: center; }
  .front-brand {
    width: 280px;
    flex: none;
    display: flex;
    align-items: center;
    gap: 10px;
    padding: 52px 0 0 36px;
  }
  .brand-dot {
    width: 28px; height: 28px;
    border-radius: 50%;
    background: var(--accent-blue);
    flex: none;
  }
  .brand-name {
    font-family: var(--brand-font);
    font-weight: 700;
    font-size: 17px;
    letter-spacing: 0.4px;
    color: var(--text-white);
    white-space: nowrap;
  }
  .divider {
    width: 1px;
    height: 128px;
    background: var(--rule);
    flex: none;
  }
  .contact {
    padding-left: 18px;
    font-size: 13px;
    line-height: 1.45;
    white-space: nowrap;
  }
  .contact-name {
    font-weight: 700;
    font-size: 15px;
    color: var(--accent-blue);
    letter-spacing: 0.5px;
    text-transform: uppercase;
  }
  .contact-title { margin-bottom: 6px; }
  .contact-address { margin-bottom: 6px; }
  .contact-row { display: flex; align-items: center; gap: 7px; }
  .contact-row svg { width: 11px; height: 11px; flex: none; }

  /* Back */
  .card-back .back-brand {
    position: absolute;
    right: 40px;
    top: 168px;
    font-family: var(--brand-font);
    font-weight: 700;
    font-size: 30px;
    letter-spacing: 1px;
    color: var(--text-white);
    white-space: nowrap;
  }
</style>
</head>
<body>
  <section class="card card-front" aria-label="Business card front">
    <div class="front-brand">
      <span class="brand-dot"></span>
      <span class="brand-name">HARBORLINE CARE</span>
    </div>
    <div class="divider"></div>
    <div class="contact">
      <p class="contact-name">Daniel Reyes</p>
      <p class="contact-title">Manager</p>
      <p class="contact-address">Your address, city<br>state, ZIP 0000</p>
      <p class="contact-row">
        <svg viewBox="0 0 12 12" aria-hidden="true"><path d="M2.5 1 L4.5 1 L5 3.5 L3.8 4.4 Q5 7 7.6 8.2 L8.5 7 L11 7.5 L11 9.5 Q11 11 9.5 11 Q1 10 1 2.5 Q1 1 2.5 1Z" fill="var(--accent-blue)"/></svg>
        555-238-7410
      </p>
      <p class="contact-row">
        <svg viewBox="0 0 12 12" aria-hidden="true"><rect x="1" y="2.5" width="10" height="7" fill="none" stroke="var(--accent-blue)" stroke-width="1.2"/><path d="M1 2.5 L6 6.5 L11 2.5" fill="none" stroke="var(--accent-blue)" stroke-width="1.2"/></svg>
        daniel@harborlinecare.com
      </p>
      <p class="contact-row">
        <svg viewBox="0 0 12 12" aria-hidden="true"><circle cx="6" cy="6" r="5" fill="var(--accent-blue)"/><path d="M1 6 H11 M6 1 Q3 6 6 11 M6 1 Q9 6 6 11" fill="none" stroke="var(--card-navy)" stroke-width="0.8"/></svg>
        www.harborlinecare.com
      </p>
    </div>
  </section>

  <section class="card card-back" aria-label="Business card back">
    <span class="back-brand">HARBORLINE CARE</span>
  </section>
</body>
</html>
```